A need a professional website for An IT Company

We need a very professional but clean wordpress design for our website.
We are into IT solutions, we manage serrvers, unified communications and do computer repairs and maintenance. We want a wordpress design that will promote our offering and online presense greatly. Our design should be very clean and mordern for easy navigation.
- A frontpage slider
contact form with Google map integration

```html
<!DOCTYPE html>
<html lang="en">
<head>
<meta charset="utf-8">
<title>Norvale — Our Services</title>
<link href="https://fonts.googleapis.com/css2?family=Arimo:wght@400;700&family=Questrial&display=swap" rel="stylesheet">
<style>
  :root{
    --plum:#6b4450;
    --plum-text:#6e3b4b;
    --ink:#222;
    --muted:#9a9a9a;
    --rule:#c9c9c9;
    --pointer:#8fa27a;
    --paper:#fff;
    --footer-top:#ececec;
    --footer-bottom:#d6d6d6;
    --social:#3c6ea6;
    --social-light:#4fb6e3;
    --badge:#1f77b8;
  }
  *{box-sizing:border-box;margin:0;padding:0}
  html,body{width:1142px;height:1200px;overflow:hidden;background:var(--paper)}
  body{position:relative;font-family:"Arimo",Arial,sans-serif;color:var(--ink)}
  a{text-decoration:none;color:inherit}

  .brand{position:absolute;left:18px;top:42px}
  .brand-name{display:block;font-size:34px;font-weight:700;color:var(--ink);letter-spacing:2px;line-height:1}
  .brand-tagline{display:block;margin-top:8px;font-size:12px;color:var(--muted)}

  .follow{position:absolute;right:30px;top:32px;display:flex;align-items:center;gap:4px;font-size:14px;color:#555}
  .follow span{margin-right:4px}
  .social{width:27px;height:27px;border-radius:4px;background:var(--social)}
  .social.light{background:var(--social-light)}

  .badge{position:absolute;left:745px;top:64px;width:90px;height:40px;border-radius:4px;background:var(--badge);opacity:.85}
  .head-divider{position:absolute;left:856px;top:66px;width:1px;height:30px;background:var(--rule)}
  .call{position:absolute;left:876px;top:70px;font-family:"Questrial",sans-serif;font-size:19px;font-style:italic;color:#333}
  .call em{color:var(--plum-text)}

  .nav{position:absolute;left:18px;top:116px;width:1102px;height:41px;background:var(--plum);border-radius:5px}
  .nav ul{list-style:none}
  .nav li{position:absolute;top:0;height:41px;line-height:41px;font-size:16px;color:#fff;transform:translateX(-50%)}
  .nav li.active{background:linear-gradient(#fff,#e6e6e6);color:#333;width:96px;text-align:center;top:2px;height:37px;line-height:37px}
  .nav-pointer{position:absolute;left:262px;top:116px;z-index:2}
  .search{position:absolute;left:880px;top:8px;width:210px;height:26px;background:#fff;border-radius:3px;font-size:12px;color:#bbb;padding:4px 6px}
  .search-btn{position:absolute;right:0;top:0;width:28px;height:26px;border-left:1px solid #ccc}

  .sidebar{position:absolute;left:18px;top:198px;width:169px;list-style:none}
  .sidebar li{height:36.5px;border-bottom:1px dashed var(--rule);font-size:15px;font-weight:700;color:var(--plum-text);padding-top:6px}
  .column-rule{position:absolute;left:216px;top:179px;height:929px;border-left:1px dashed var(--rule)}

  .page-title{position:absolute;left:231px;top:172px;font-family:"Questrial",sans-serif;font-weight:400;font-size:24px;color:var(--plum-text)}
  .title-rule{position:absolute;left:231px;top:206px;width:886px;height:24px;border-top:1px solid var(--rule);background:linear-gradient(#f0f0f0,#fff)}

  .service{position:absolute;left:235px;width:888px}
  .service h2{font-size:20px;font-weight:700;color:var(--plum-text);margin-bottom:6px}
  .service p{font-size:14px;line-height:20.5px;color:var(--ink);letter-spacing:.5px}

  .footer{position:absolute;left:18px;top:1125px;width:1102px;height:41px;background:linear-gradient(var(--footer-top),var(--footer-bottom));font-size:14px;color:#555;display:flex;align-items:center;justify-content:space-between;padding:0 14px 0 18px}
  .footer .copy{color:var(--muted)}
  .footer nav a+a::before{content:"I";margin:0 12px;font-size:11px}
</style>
</head>
<body>
  <header>
    <div class="brand">
      <span class="brand-name">NORVALE</span>
      <span class="brand-tagline">...dependable IT support</span>
    </div>
    <div class="follow"><span>Follow us:</span><i class="social"></i><i class="social"></i><i class="social light"></i></div>
    <div class="badge" role="img" aria-label="Partner certification badge"></div>
    <div class="head-divider"></div>
    <div class="call"><em>Call us :</em> +(234) 700-555-0142</div>
  </header>

  <nav class="nav">
    <ul>
      <li style="left:54px">Home</li>
      <li style="left:153px">About</li>
      <li class="active" style="left:254px">Services</li>
      <li style="left:362px">Clients</li>
      <li style="left:451px">Blog</li>
      <li style="left:556px">Contact Us</li>
      <li style="left:674px">Sitemap</li>
    </ul>
    <div class="search">Search
      <span class="search-btn"><svg width="28" height="26" viewBox="0 0 28 26"><circle cx="13" cy="12" r="5" fill="none" stroke="#333" stroke-width="2"/><path d="M16.5 15.5l4 4" stroke="#333" stroke-width="2.4"/></svg></span>
    </div>
  </nav>
  <svg class="nav-pointer" width="12" height="8" viewBox="0 0 12 8"><path d="M0 0h12L6 8z" fill="var(--pointer)"/></svg>

  <ul class="sidebar">
    <li>Computer Consultancy</li>
    <li>Computer Training</li>
    <li>Computer software</li>
    <li>Computer Consultancy</li>
    <li>Computer Training</li>
    <li>Computer software</li>
  </ul>
  <div class="column-rule"></div>

  <main>
    <h1 class="page-title">Our Services</h1>
    <div class="title-rule"></div>

    <section class="service" style="top:232px"><h2>Praesent vestibulum molestie lacus. Aenean nonummy</h2><p>Praesent vestibulum molestie lacus. Aenean nonummy hendrerit mauris. Phasellus porta. Fusce suscipit varius mi. Cum sociis natoque penatibus et magnis dis parturient montes, nascetur ridiculus mus. Nulla dui. Fusce feugiat malesuada odio. Morbi nunc odio, gravida at, cursus nec, luctus a, lorem. Maecenas tristique orci ac sem. Duis ultricies pharetra magna. Donec accumsan malesuada orci. Donec sit amet eros.</p></section>
    <section class="service" style="top:369px"><h2>Praesent vestibulum molestie lacus. Aenean nonummy</h2><p>Praesent vestibulum molestie lacus. Aenean nonummy hendrerit mauris. Phasellus porta. Fusce suscipit varius mi. Cum sociis natoque penatibus et magnis dis parturient montes, nascetur ridiculus mus. Nulla dui. Fusce feugiat malesuada odio. Morbi nunc odio, gravida at, cursus nec, luctus a, lorem. Maecenas tristique orci ac sem. Duis ultricies pharetra magna. Donec accumsan malesuada orci. Donec sit amet eros.</p></section>
    <section class="service" style="top:506px"><h2>Praesent vestibulum molestie lacus. Aenean nonummy</h2><p>Praesent vestibulum molestie lacus. Aenean nonummy hendrerit mauris. Phasellus porta. Fusce suscipit varius mi. Cum sociis natoque penatibus et magnis dis parturient montes, nascetur ridiculus mus. Nulla dui. Fusce feugiat malesuada odio. Morbi nunc odio, gravida at, cursus nec, luctus a, lorem. Maecenas tristique orci ac sem. Duis ultricies pharetra magna. Donec accumsan malesuada orci. Donec sit amet eros.</p></section>
    <section class="service" style="top:666px"><h2>Praesent vestibulum molestie lacus. Aenean nonummy</h2><p>Praesent vestibulum molestie lacus. Aenean nonummy hendrerit mauris. Phasellus porta. Fusce suscipit varius mi. Cum sociis natoque penatibus et magnis dis parturient montes, nascetur ridiculus mus. Nulla dui. Fusce feugiat malesuada odio. Morbi nunc odio, gravida at, cursus nec, luctus a, lorem. Maecenas tristique orci ac sem. Duis ultricies pharetra magna. Donec accumsan malesuada orci. Donec sit amet eros.</p></section>
    <section class="service" style="top:826px"><h2>Praesent vestibulum molestie lacus. Aenean nonummy</h2><p>Praesent vestibulum molestie lacus. Aenean nonummy hendrerit mauris. Phasellus porta. Fusce suscipit varius mi. Cum sociis natoque penatibus et magnis dis parturient montes, nascetur ridiculus mus. Nulla dui. Fusce feugiat malesuada odio. Morbi nunc odio, gravida at, cursus nec, luctus a, lorem. Maecenas tristique orci ac sem. Duis ultricies pharetra magna. Donec accumsan malesuada orci. Donec sit amet eros.</p></section>
    <section class="service" style="top:977px"><h2>Praesent vestibulum molestie lacus. Aenean nonummy</h2><p>Praesent vestibulum molestie lacus. Aenean nonummy hendrerit mauris. Phasellus porta. Fusce suscipit varius mi. Cum sociis natoque penatibus et magnis dis parturient montes, nascetur ridiculus mus. Nulla dui. Fusce feugiat malesuada odio. Morbi nunc odio, gravida at, cursus nec, luctus a, lorem. Maecenas tristique orci ac sem. Duis ultricies pharetra magna. Donec accumsan malesuada orci. Donec sit amet eros.</p></section>
  </main>

  <footer class="footer">
    <span class="copy">© 2012 Norvale Solutions Limited.</span>
    <nav><a>Home</a><a>About</a><a>Services</a><a>Clients</a><a>Blog</a><a>Contact Us</a><a>Sitemap</a></nav>
  </footer>
</body>
</html>
```